Business Card Design for a Sound engineer and DJ

We would like a residn of the business card.

Logo must remain the same.
The card is for the owner of the company.
The business card is in Arabic as the company is based in Kuwait.
The company specializes in sound engineering for singers concerts and events and in addition DJ.
The color options is up to the designer but we would like it masculine as the owner is a man.

Target Market(s)

All ages

Industry/Entity Type

Media

Contact Information for Business Card

Name:
Eng. Tarek Halabi
م/طارق حلبي

The name above is in Arabic and English.

Title: General Manager
Mobile: +965 66307852
Office: +965 22486037
Email: info@sawtarin.net

Address:
Office no. 3
1st floor
Almarfa Complex
Rashed AlQeblawi St.
Salmiya
Kuwait

Instagram: @sawtarin
Snap: sawtarin

Requirements
Nice to have
• can we have Instagram icon and snap icon and a phone vector and email?
• Instead of writing the words

```html
<!DOCTYPE html>
<html lang="en">
<head>
<meta charset="utf-8">
<title>Sawtarin — Business Card</title>
<link rel="stylesheet" href="https://fonts.googleapis.com/css2?family=Source+Sans+3:wght@400;600;700&family=Cairo:wght@600;700&display=swap">
<style>
  :root {
    --stage: #1b1b1b;
    --card: #ffffff;
    --pink: #e5288c;
    --purple: #7a3a9e;
    --blue: #4b5fb3;
    --ink: #333333;
  }
  * { margin: 0; padding: 0; box-sizing: border-box; }
  html, body { width: 1200px; height: 900px; overflow: hidden; }
  body {
    background: var(--stage);
    font-family: "Source Sans 3", Arial, sans-serif;
    position: relative;
  }
  .card {
    position: absolute;
    top: 170px;
    width: 347px;
    height: 561px;
    background: var(--card);
    text-align: center;
  }
  .card--front { left: 259px; }
  .card--back { left: 631px; }

  .band {
    position: absolute;
    left: 102px;
    width: 143px;
    height: 29px;
    background: var(--pink);
  }
  .band--top { top: 0; }
  .band--bottom { bottom: 0; }

  .brand {
    position: absolute;
    left: 0; right: 0;
  }
  .brand__name {
    display: inline-flex;
    align-items: center;
    gap: 10px;
    color: var(--purple);
    font-weight: 600;
    letter-spacing: 6px;
    line-height: 1;
  }
  .brand__dot {
    width: 12px; height: 12px;
    border-radius: 50%;
    background: var(--pink);
    flex: none;
  }
  .brand__tagline {
    color: var(--purple);
    font-weight: 700;
    letter-spacing: 1.6px;
    line-height: 1;
  }
  .brand__tagline-ar {
    font-family: "Cairo", "Source Sans 3", sans-serif;
    color: var(--purple);
    font-weight: 700;
    line-height: 1.1;
    direction: rtl;
  }

  .card--front .brand { top: 198px; }
  .card--front .brand__name { font-size: 28px; }
  .card--front .brand__tagline { font-size: 12.5px; margin-top: 6px; }
  .card--front .brand__tagline-ar { font-size: 14px; margin-top: 3px; }

  .card--back .brand { top: 284px; }
  .card--back .brand__name { font-size: 34px; }
  .card--back .brand__tagline { font-size: 14px; margin-top: 8px; }
  .card--back .brand__tagline-ar { font-size: 16px; margin-top: 4px; }

  .person { position: absolute; top: 292px; left: 0; right: 0; }
  .person__name { color: var(--pink); font-size: 21px; font-weight: 600; line-height: 1; }
  .person__name-ar {
    font-family: "Cairo", "Source Sans 3", sans-serif;
    color: var(--pink); font-size: 15px; font-weight: 600;
    line-height: 1.2; margin-top: 4px; direction: rtl;
  }
  .person__title { color: var(--blue); font-size: 16px; margin-top: 12px; line-height: 1; }

  .contact {
    position: absolute; top: 384px; left: 0; right: 0;
    list-style: none;
    color: var(--ink); font-size: 16px;
  }
  .contact__item {
    display: flex; justify-content: center; align-items: center;
    gap: 9px; height: 23px;
  }
  .contact__icon { width: 11px; height: 11px; fill: var(--pink); flex: none; }

  .address {
    position: absolute; top: 463px; left: 0; right: 0;
    color: var(--ink); font-size: 16px; line-height: 21px; font-style: normal;
  }

  .social {
    position: absolute; top: 435px; left: 0; right: 0;
    display: flex; justify-content: center; gap: 16px;
    list-style: none; color: var(--ink); font-size: 16px;
  }
  .social__item { display: flex; align-items: center; gap: 7px; }
  .social__mark { width: 11px; height: 11px; background: var(--pink); border-radius: 2px; }
</style>
</head>
<body>

<section class="card card--front">
  <div class="band band--top"></div>

  <div class="brand">
    <div class="brand__name"><span class="brand__dot"></span>SAWTARIN</div>
    <div class="brand__tagline">DJ - SOUND ENG. - LIGHTING</div>
    <div class="brand__tagline-ar">دي جي - هندسة صوت - إضاءة</div>
  </div>

  <div class="person">
    <div class="person__name">Eng. Tarek Halabi</div>
    <div class="person__name-ar">م/طارق حلبي</div>
    <div class="person__title">General Manager</div>
  </div>

  <ul class="contact">
    <li class="contact__item">
      <svg class="contact__icon" viewBox="0 0 12 12" aria-hidden="true"><path d="M3 0h6a1 1 0 0 1 1 1v10a1 1 0 0 1-1 1H3a1 1 0 0 1-1-1V1a1 1 0 0 1 1-1zm.6 1.4v8h4.8v-8z"/></svg>
      +965 66307852
    </li>
    <li class="contact__item">
      <svg class="contact__icon" viewBox="0 0 12 12" aria-hidden="true"><path d="M2.4 0.5 4.3 2.6 3.3 4.1c.8 1.8 2.4 3.4 4.3 4.4l1.4-1.1 2.1 1.9-.9 2C6.5 11.5.5 5.6.4 1.6z"/></svg>
      +965 22486037
    </li>
    <li class="contact__item">
      <svg class="contact__icon" viewBox="0 0 12 12" aria-hidden="true"><path d="M0 2h12v1.2L6 7 0 3.2zM0 4.6l6 3.8 6-3.8V10H0z"/></svg>
      info@sawtarin.net
    </li>
  </ul>

  <address class="address">
    Office no. 3 1st floor Almarfa<br>
    Complex Rashed AlQeblawi St. Salmiya Kuwait
  </address>

  <div class="band band--bottom"></div>
</section>

<section class="card card--back">
  <div class="brand">
    <div class="brand__name"><span class="brand__dot"></span>SAWTARIN</div>
    <div class="brand__tagline">DJ - SOUND ENG. - LIGHTING</div>
    <div class="brand__tagline-ar">دي جي - هندسة صوت - إضاءة</div>
  </div>

  <ul class="social">
    <li class="social__item"><span class="social__mark"></span>@sawtarin</li>
    <li class="social__item"><span class="social__mark"></span>sawtarin</li>
  </ul>
</section>

</body>
</html>
```